Kes-Trindle web design

We need a homepage web design with final files to be provided in PSD for a company based in Brisbane called 'Kes-Trindle'. They provide innovative and reliable contract packaging solutions for local and national outsourcing buisnesses.

They have an existing website www.kes-trindle.com.au that is in dire need of an update to look more professional and sleek.

Target Market(s)

Engineers, Architects

Industry/Entity Type

Construction

Number of Pages Required

1 page

Requirements
Must have
• Main Navigation
• o Home
• o About Us
• o Spacers
• - Standard Cage Wheel Spacer
• - Heavy Duty Cage Wheel Spacer
• - Pile Cage Foot
• - PreCast Piles
• o Packaging
• o Injection Moulding
• o News
• o Contact Us
• - Client wants an updated more professional look and feel that aligns with their branding.
• - Client likes the use of displaying Products on every page eg www.gravelnook.com that has an image of the product and its name obviously looking better than this.
• The following elements are to be included in the Homepage design concept:
• - Room for a Flash banner of rotating images
• - Horizontal navigation (can you show how drop down will appear as well)
• - Logo is attached
• - Phone number needs to appear prominently on every page 07 3190 4856
• - Use Arial font throughout concept incl logo
• - Intro text on page somewhere
• - Products need to be listed on page somewhere there are 7 products (image and name with click through)
• - 2 containers/icons to highlight areas on site Latest News and Contact Us
• - Images – have attached a few that can be used in concepts and also below are some pixmarrow images that could be used in banner:
• http://www.pixmarrowfoto.com/stock-photo-4820316-several-paint-buckets.php
• http://www.pixmarrowfoto.com/stock-photo-3157840-cans-of-paint.php
• http://www.pixmarrowfoto.com/stock-photo-2748391-reinforcing-steel.php
• http://www.pixmarrowfoto.com/stock-photo-8063412-huge-bridge-pier.php
• http://www.pixmarrowfoto.com/stock-photo-1592874-highway-bridge.php
• http://www.pixmarrowfoto.com/stock-photo-4306159-bridge.php
• http://www.pixmarrowfoto.com/stock-photo-2684037-bridge-to-nowhere-yet.php

```html
<!DOCTYPE html>
<html lang="en">
<head>
<meta charset="utf-8">
<title>Kes-Trindle — Homepage and Content Page</title>
<link href="https://fonts.googleapis.com/css2?family=Arimo:wght@400;700&family=Oswald:wght@600&display=swap" rel="stylesheet">
<style>
:root{
  --red:#c4161c;
  --red-dark:#8c0a0e;
  --frame-red:#a50d10;
  --black:#070707;
  --panel-dark:#454545;
  --panel-darker:#3a3a3a;
  --text-light:#f2f2f2;
  --text-soft:#e4e4e4;
  --nav-text:#1d1d1d;
  --white:#ffffff;
}
*{margin:0;padding:0;box-sizing:border-box}
html,body{width:1200px;height:3458px;overflow:hidden}
body{position:relative;background:var(--white);font-family:Arimo,Arial,sans-serif;color:var(--text-light)}
.page{position:absolute;left:0;width:1200px;background:var(--frame-red)}
.page--home{top:0;height:1660px}
.page--content{top:1678px;height:1780px}
.page__inner{position:absolute;left:16px;right:16px;top:0;bottom:0;overflow:hidden;
  background:linear-gradient(180deg,#555 0,#666 30%,#a5a5a5 75%,#c4c4c4 100%)}

/* header */
.header{position:absolute;left:0;right:0;top:0;height:175px;
  background:linear-gradient(180deg,#2a2a2a 0,#0c0c0c 45%,#3b3b3b 100%)}
.brand{position:absolute;left:84px;top:11px;display:flex;align-items:flex-end}
.brand__mark{width:137px;height:137px;border-radius:50%;background:radial-gradient(circle at 40% 35%,#e23a3a 0,var(--red) 45%,var(--red-dark) 100%)}
.brand__name{position:absolute;left:106px;top:88px;font-size:20px;font-weight:700;color:#cfcfcf;white-space:nowrap}
.phone{position:absolute;left:794px;top:56px;width:301px;height:62px;border-radius:8px;
  background:linear-gradient(180deg,#e23030,var(--red) 55%,#9c0f12);border:2px solid #e87070;
  display:flex;align-items:center;justify-content:center;gap:8px;
  font-family:Oswald,Impact,sans-serif;font-weight:600;font-size:42px;color:var(--white);letter-spacing:.5px}
.phone svg{width:18px;height:30px}

/* nav */
.nav{position:absolute;left:0;right:0;top:175px;height:42px;
  background:linear-gradient(180deg,#d9d9d9,#9c9c9c 55%,#7d7d7d);display:flex;align-items:center;padding-left:190px}
.nav__item{font-size:13px;font-weight:700;color:var(--white);text-shadow:0 1px 1px #333;padding:0 21px;position:relative}
.nav__item+.nav__item::before{content:"";position:absolute;left:0;top:1px;height:13px;border-left:1px solid #555}
.dropdown{position:absolute;left:381px;top:208px;width:199px;z-index:3}
.dropdown__item{height:21px;font-size:13px;color:var(--white);text-align:center;line-height:21px;
  background:linear-gradient(180deg,#3a3a3a,#111);border-bottom:1px solid #555}
.dropdown__item--active{background:linear-gradient(180deg,#e23030,#a31216);color:#fff;font-weight:700}

.banner{position:absolute;left:0;right:0;top:217px;height:302px;
  background:linear-gradient(90deg,#5f7fa8 0,#b7c0c7 14%,#8e8d8a 30%,#d4d2cc 45%,#7a818b 58%,#a6784d 70%,#c0392b 80%,#e4c42a 88%,#1f47b0 100%)}

/* buttons */
.btn{display:inline-block;border-radius:14px;border:2px solid #cfcfcf;
  background:linear-gradient(180deg,#8c8c8c,#2d2d2d 55%,#1c1c1c);color:var(--white);font-weight:700;text-align:center}
.btn--lg{width:149px;height:35px;line-height:31px;font-size:19px}
.btn--sm{width:128px;height:27px;line-height:23px;font-size:16px}
.btn--xs{width:95px;height:20px;line-height:16px;font-size:12px}

/* intro */
.intro{position:absolute;left:35px;top:41px;width:660px}
.intro h1,.section-title{font-size:19px;font-weight:700;color:var(--white)}
.intro p{font-size:13px;line-height:16px;margin-top:10px;color:var(--text-soft)}
.intro p+p{margin-top:17px}

/* product list */
.products{position:absolute;border-radius:18px;background:var(--panel-dark)}
.product{position:absolute;left:48px}
.product__thumb{position:absolute;left:0;top:0;width:100px;height:84px;border:2px solid #ddd;
  background:radial-gradient(circle at 50% 45%,#ffffff 0,#e2e2e2 55%,#a9a9a9 100%)}
.product__info{position:absolute;left:112px;top:27px;width:309px}
.product__name{font-size:17px;font-weight:700;font-variant:small-caps;letter-spacing:1px;color:var(--white);
  padding-bottom:4px;border-bottom:2px dotted #9a9a9a}
.product__info .btn{position:absolute;right:0;top:34px}

.products--compact .product{left:40px}
.products--compact .product__thumb{width:74px;height:62px}
.products--compact .product__info{left:84px;top:20px;width:235px}
.products--compact .product__name{font-size:12.5px;letter-spacing:.6px;padding-bottom:3px}
.products--compact .product__info .btn{top:25px}

/* feature */
.feature{position:absolute;left:717px;top:26px;width:425px;height:388px;border-radius:16px;background:var(--panel-darker);overflow:hidden}
.feature__title{height:44px;line-height:50px;text-align:center;font-size:20px;font-weight:700;font-variant:small-caps;letter-spacing:1px;
  background:linear-gradient(180deg,#6a6a6a,#3a3a3a)}
.feature__image{position:absolute;left:107px;top:70px;width:169px;height:167px;border-radius:8px;background:radial-gradient(circle,#fff 0,#e8e8e8 70%,#cfcfcf 100%)}
.feature__arrow{position:absolute;top:130px;width:34px;height:34px}
.feature__arrow--prev{left:64px}.feature__arrow--next{left:326px}
.feature__text{position:absolute;left:14px;right:14px;top:253px;text-align:center;font-size:16px;line-height:19px;color:var(--text-soft)}
.feature .btn{position:absolute;left:139px;top:337px}

/* highlights */
.highlight{position:absolute;left:778px;display:flex;align-items:center;gap:12px;font-size:29px;color:var(--white);letter-spacing:.5px}
.highlight svg{width:78px;height:78px}
.badge{position:absolute;border-radius:8px;background:var(--white)}

/* content page */
.article{position:absolute;left:30px;top:41px;width:680px}
.article p{font-size:13.4px;line-height:16px;margin-top:10px;color:var(--text-soft)}
.article p+p{margin-top:16px}
.article .btn{position:absolute;left:535px;top:403px}
.scroll-panel{position:absolute;left:26px;top:1017px;width:680px;height:602px;border-radius:22px;
  background:linear-gradient(180deg,#cfcfcf 0,#9b9b9b 12%,#8e8e8e 100%)}
.scroll-panel h2{position:absolute;left:25px;top:18px;font-size:19px;font-weight:700;color:#222}
.scroll-panel__body{position:absolute;left:26px;top:74px;width:590px}
.scroll-panel__body p{font-size:13.2px;line-height:16px;color:var(--white)}
.scroll-panel__body p+p{margin-top:16px}
.scroll-track{position:absolute;left:626px;top:32px;width:27px;height:548px;border-radius:13px;background:#b5b5b5}
.scroll-thumb{position:absolute;left:0;top:92px;width:27px;height:67px;background:#8a8a8a}

/* footer */
.footer{position:absolute;left:0;right:0;bottom:0;background:var(--black);text-align:right;padding-right:18px;font-size:13px;font-weight:700;color:var(--white)}
.page--home .footer{height:123px;padding-top:20px}
.page--content .footer{height:130px;padding-top:26px}
.footer__line{line-height:22px}
.footer__nav span+span::before{content:"|";color:#777;margin:0 6px;font-weight:400}
</style>
</head>
<body>

<!-- ============ HOME PAGE ============ -->
<section class="page page--home">
  <div class="page__inner">
    <header class="header">
      <div class="brand"><div class="brand__mark"></div><div class="brand__name">Kes-Trindle</div></div>
      <div class="phone">
        <svg viewBox="0 0 18 30"><rect x="1.5" y="1.5" width="15" height="27" rx="3" fill="none" stroke="#fff" stroke-width="2.5"/><rect x="5" y="5" width="8" height="13" fill="#fff"/><circle cx="9" cy="23" r="2" fill="#fff"/></svg>
        07 3190 4856
      </div>
    </header>
    <nav class="nav">
      <span class="nav__item">HOME</span><span class="nav__item">ABOUT US</span><span class="nav__item">SPACERS</span><span class="nav__item">PACKAGING</span><span class="nav__item">INJECTION MOULDING</span><span class="nav__item">NEWS</span><span class="nav__item">CONTACT US</span>
    </nav>
    <div class="dropdown">
      <div class="dropdown__item">Standard Cage Wheel Spacer</div>
      <div class="dropdown__item dropdown__item--active">Heavy Duty Cage Wheel Spacer</div>
      <div class="dropdown__item">Pile Cage Foot</div>
      <div class="dropdown__item">PreCast Piles</div>
    </div>
    <div class="banner" role="img" aria-label="Rotating banner: highway bridge piers, reinforcing steel cage and paint buckets"></div>

    <main style="position:absolute;left:0;right:0;top:519px">
      <div class="intro">
        <h1>WELCOME TO Kes-Trindle!</h1>
        <p>Kes-Trindle Brisbane, providing innovative and reliable contract packaging solutions for local and national outsourcing buisnesses.</p>
        <p>Kes-Trindle (QLD) PTY LTD is a wholly Australian business with a firm foundation in client relations which we feel is of utmost import with an ever-expanding customer base. As such we endeavour to hold true to our founding company objectives and look towards the future with great confidence.</p>
      </div>
      <span class="btn btn--lg" style="position:absolute;left:521px;top:168px">read more</span>
      <h2 class="section-title" style="position:absolute;left:35px;top:206px">Kes-Trindle' Products</h2>

      <section class="products" style="left:103px;top:242px;width:516px;height:715px">
        <div class="product" style="top:24px"><div class="product__thumb" role="img" aria-label="Hinged pile wheel"></div><div class="product__info"><div class="product__name">Hinged Pile Wheel</div><span class="btn btn--sm">read more</span></div></div>
        <div class="product" style="top:121px"><div class="product__thumb" role="img" aria-label="Precast pile chair"></div><div class="product__info"><div class="product__name">Precast Pile Chair</div><span class="btn btn--sm">read more</span></div></div>
        <div class="product" style="top:218px"><div class="product__thumb" role="img" aria-label="Pipe plug"></div><div class="product__info"><div class="product__name">Pipe Plugs</div><span class="btn btn--sm">read more</span></div></div>
        <div class="product" style="top:317px"><div class="product__thumb" role="img" aria-label="Containers and lids"></div><div class="product__info"><div class="product__name">Containers &amp; Lids</div><span class="btn btn--sm">read more</span></div></div>
        <div class="product" style="top:413px"><div class="product__thumb" role="img" aria-label="End cap"></div><div class="product__info"><div class="product__name">End Cap</div><span class="btn btn--sm">read more</span></div></div>
        <div class="product" style="top:510px"><div class="product__thumb" role="img" aria-label="Light weight web wheel"></div><div class="product__info"><div class="product__name">Light Weight Web Wheel</div><span class="btn btn--sm">read more</span></div></div>
        <div class="product" style="top:607px"><div class="product__thumb" role="img" aria-label="Heavy duty wheel spacer"></div><div class="product__info"><div class="product__name">Heavy Duty wheel Spacer</div><span class="btn btn--sm">read more</span></div></div>
      </section>

      <section class="feature">
        <div class="feature__title">Hinged Pile Wheel for Cages</div>
        <svg class="feature__arrow feature__arrow--prev" viewBox="0 0 34 34"><path d="M17 6 6 17l11 11M28 6 17 17l11 11" fill="none" stroke="#bbb" stroke-width="5"/></svg>
        <div class="feature__image" role="img" aria-label="Hinged pile wheel product photo"></div>
        <svg class="feature__arrow feature__arrow--next" viewBox="0 0 34 34"><path d="M6 6l11 11L6 28M17 6l11 11-11 11" fill="none" stroke="#bbb" stroke-width="5"/></svg>
        <p class="feature__text">Kes-Trindle' Hinged Pile Wheels are innovativly designed for most types of heavy-duty applications. They are available in 150mm and 100mm wheel diameters for 75mm and 50mm cover respectively.</p>
        <span class="btn btn--lg">more info</span>
      </section>

      <div class="highlight" style="top:440px">
        <svg viewBox="0 0 78 78"><circle cx="39" cy="39" r="38" fill="var(--red)"/><circle cx="39" cy="39" r="27" fill="#fff"/><rect x="31" y="22" width="16" height="34" rx="3" fill="var(--red)"/><rect x="35" y="27" width="8" height="24" fill="#fff"/></svg>
        <span>CONTACT US</span>
      </div>
      <div class="highlight" style="top:516px">
        <svg viewBox="0 0 78 78"><circle cx="39" cy="39" r="38" fill="var(--red)"/><path d="M26 18h20l8 8v34H26z" fill="#fff"/><path d="M31 32h18M31 38h18M31 44h18M31 50h18" stroke="var(--red)" stroke-width="2.5"/></svg>
        <span>LATEST NEWS</span>
      </div>
      <div class="badge" style="left:850px;top:603px;width:159px;height:144px"></div>
    </main>

    <footer class="footer">
      <div class="footer__line">LOGIN</div>
      <div class="footer__line footer__nav"><span>HOME</span><span>ABOUT US</span><span>SPACERS</span><span>PACKAGING</span><span>INJECTION MOULDING</span><span>NEWS</span><span>CONTACT US</span></div>
      <div class="footer__line">© 2009 KES-TRINDLE.com.au | All Rights Reserved</div>
    </footer>
  </div>
</section>

<!-- ============ CONTENT PAGE ============ -->
<section class="page page--content">
  <div class="page__inner">
    <header class="header">
      <div class="brand"><div class="brand__mark"></div><div class="brand__name">Kes-Trindle</div></div>
      <div class="phone">
        <svg viewBox="0 0 18 30"><rect x="1.5" y="1.5" width="15" height="27" rx="3" fill="none" stroke="#fff" stroke-width="2.5"/><rect x="5" y="5" width="8" height="13" fill="#fff"/><circle cx="9" cy="23" r="2" fill="#fff"/></svg>
        07 3190 4856
      </div>
    </header>
    <nav class="nav">
      <span class="nav__item">HOME</span><span class="nav__item">ABOUT US</span><span class="nav__item">SPACERS</span><span class="nav__item">PACKAGING</span><span class="nav__item">INJECTION MOULDING</span><span class="nav__item">NEWS</span><span class="nav__item">CONTACT US</span>
    </nav>
    <div class="dropdown">
      <div class="dropdown__item">Standard Cage Wheel Spacer</div>
      <div class="dropdown__item dropdown__item--active">Heavy Duty Cage Wheel Spacer</div>
      <div class="dropdown__item">Pile Cage Foot</div>
      <div class="dropdown__item">PreCast Piles</div>
    </div>
    <div class="banner" role="img" aria-label="Rotating banner: highway bridge piers, reinforcing steel cage and paint buckets"></div>

    <main style="position:absolute;left:0;right:0;top:519px;bottom:130px">
      <article class="article">
        <h1 class="section-title">Content Page!</h1>
        <p>Lorem ipsum dolor sit amet, consetetur sadipscing elitr, sed diam nonumy eirmod tempor invidunt<br>ut labore et dolore magna aliquyam erat, sed diam voluptua.</p>
        <p>At vero eos et accusam et justo duo dolores et ea rebum. Stet clita kasd gubergren, no sea takimata<br>sanctus est Lorem ipsum dolor sit amet. Lorem ipsum dolor sit amet, consetetur sadipscing elitr,<br>sed diam nonum.</p>
        <p>Lorem ipsum dolor sit amet, consetetur sadipscing elitr, sed diam nonumy eirmod tempor invidunt<br>ut labore et dolore magna aliquyam erat, sed diam voluptua. At vero eos et accusam et justo duo dolores<br>et ea rebum. Stet clita kasd gubergren, no sea takimata sanctus est Lorem ipsum dolor sit amet. Lorem<br>ipsum dolor sit amet, consetetur sadipscing elitr, sed diam nonum.</p>
        <p>Lorem ipsum dolor sit amet, consetetur sadipscing elitr, sed diam nonumy eirmod tempor invidunt<br>ut labore et dolore magna aliquyam erat, sed diam voluptua.</p>
        <p>At vero eos et accusam et justo duo dolores et ea rebum. Stet clita kasd gubergren, no sea takimata<br>sanctus est Lorem ipsum dolor sit amet. Lorem ipsum dolor sit amet, consetetur sadipscing elitr,<br>sed diam nonum.</p>
        <p>Lorem ipsum dolor sit amet, consetetur sadipscing elitr, sed diam nonumy eirmod tempor invidunt<br>ut labore et dolore magna aliquyam erat, sed diam voluptua. At vero eos et accusam et justo duo dolores<br>et ea rebum. Stet clita kasd gubergren, no sea takimata sanctus est Lorem ipsum dolor sit amet. Lorem<br>ipsum dolor sit amet, consetetur sadipscing elitr, sed diam nonum.</p>
        <span class="btn btn--lg">read more</span>
      </article>

      <section class="scroll-panel" style="top:498px">
        <h2>Content Page!</h2>
        <div class="scroll-panel__body">
          <p>Lorem ipsum dolor sit amet, consetetur sadipscing elitr, sed diam nonumy eirmod tempor<br>invidunt ut labore et dolore magna aliquyam erat, sed diam voluptua.</p>
          <p>At vero eos et accusam et justo duo dolores et ea rebum. Stet clita kasd gubergren, no<br>sea takimata sanctus est Lorem ipsum dolor sit amet. Lorem ipsum dolor sit amet,<br>consetetur sadipscing elitr,<br>sed diam nonum.</p>
          <p>Lorem ipsum dolor sit amet, consetetur sadipscing elitr, sed diam nonumy eirmod tempor<br>invidunt ut labore et dolore magna aliquyam erat, sed diam voluptua.</p>
          <p>At vero eos et accusam et justo duo dolores et ea rebum. Stet clita kasd gubergren, no<br>sea takimata sanctus est Lorem ipsum dolor sit amet. Lorem ipsum dolor sit amet,<br>consetetur sadipscing elitr,<br>sed diam nonum.</p>
          <p>Lorem ipsum dolor sit amet, consetetur sadipscing elitr, sed diam nonumy eirmod tempor<br>invidunt ut labore et dolore magna aliquyam erat, sed diam voluptua.</p>
          <p>At vero eos et accusam et justo duo dolores et ea rebum. Stet clita kasd gubergren, no<br>sea takimata sanctus est Lorem ipsum dolor sit amet. Lorem ipsum dolor sit amet,<br>consetetur sadipscing elitr,<br>sed diam nonum.</p>
          <p>Lorem ipsum dolor sit amet, consetetur sadipscing elitr, sed diam nonumy eirmod tempor<br>invidunt ut labore et dolore magna aliquyam erat, sed diam voluptua.</p>
          <p>At vero eos et accusam et justo duo dolores et ea rebum. Stet clita kasd gubergren, no<br>sea takimata sanctus est Lorem ipsum dolor sit amet. Lorem ipsum dolor sit amet,<br>consetetur sadipscing elitr,<br>sed diam nonum.</p>
        </div>
        <div class="scroll-track"><div class="scroll-thumb"></div></div>
      </section>

      <h2 class="section-title" style="position:absolute;left:738px;top:41px">Kes-Trindle' Products</h2>
      <section class="products products--compact" style="left:736px;top:62px;width:395px;height:546px">
        <div class="product" style="top:20px"><div class="product__thumb" role="img" aria-label="Hinged pile wheel"></div><div class="product__info"><div class="product__name">Hinged Pile Wheel</div><span class="btn btn--xs">read more</span></div></div>
        <div class="product" style="top:94px"><div class="product__thumb" role="img" aria-label="Precast pile chair"></div><div class="product__info"><div class="product__name">Precast Pile Chair</div><span class="btn btn--xs">read more</span></div></div>
        <div class="product" style="top:168px"><div class="product__thumb" role="img" aria-label="Pipe plug"></div><div class="product__info"><div class="product__name">Pipe Plugs</div><span class="btn btn--xs">read more</span></div></div>
        <div class="product" style="top:244px"><div class="product__thumb" role="img" aria-label="Containers and lids"></div><div class="product__info"><div class="product__name">Containers &amp; Lids</div><span class="btn btn--xs">read more</span></div></div>
        <div class="product" style="top:318px"><div class="product__thumb" role="img" aria-label="End cap"></div><div class="product__info"><div class="product__name">End Cap</div><span class="btn btn--xs">read more</span></div></div>
        <div class="product" style="top:392px"><div class="product__thumb" role="img" aria-label="Light weight web wheel"></div><div class="product__info"><div class="product__name">Light Weight Web Wheel</div><span class="btn btn--xs">read more</span></div></div>
        <div class="product" style="top:466px"><div class="product__thumb" role="img" aria-label="Heavy duty wheel spacer"></div><div class="product__info"><div class="product__name">Heavy Duty wheel Spacer</div><span class="btn btn--xs">read more</span></div></div>
      </section>

      <div class="highlight" style="top:639px">
        <svg viewBox="0 0 78 78"><circle cx="39" cy="39" r="38" fill="var(--red)"/><circle cx="39" cy="39" r="27" fill="#fff"/><rect x="31" y="22" width="16" height="34" rx="3" fill="var(--red)"/><rect x="35" y="27" width="8" height="24" fill="#fff"/></svg>
        <span>CONTACT US</span>
      </div>
      <div class="highlight" style="top:714px">
        <svg viewBox="0 0 78 78"><circle cx="39" cy="39" r="38" fill="var(--red)"/><path d="M26 18h20l8 8v34H26z" fill="#fff"/><path d="M31 32h18M31 38h18M31 44h18M31 50h18" stroke="var(--red)" stroke-width="2.5"/></svg>
        <span>LATEST NEWS</span>
      </div>
      <div class="badge" style="left:872px;top:796px;width:160px;height:145px"></div>
    </main>

    <footer class="footer">
      <div class="footer__line">LOGIN</div>
      <div class="footer__line footer__nav"><span>HOME</span><span>ABOUT US</span><span>SPACERS</span><span>PACKAGING</span><span>INJECTION MOULDING</span><span>NEWS</span><span>CONTACT US</span></div>
      <div class="footer__line">© 2009 KES-TRINDLE.com.au | All Rights Reserved</div>
    </footer>
  </div>
</section>

</body>
</html>
```